KestaLaw a fully remote and fully bilingual law firm for the Florida injured

1. Can you describe what your company does?- a solo lawyer practice in Florida, D.C., and soon in NY. I offer services for auto accidents, negligence, boat accident, motorcycle accident, insurance claims, premises liability, and things of the like.

2. Who are your target customers for the website? Drivers, passengers, pedestrians involved in accidents where they were injured and need help making a claim against the other vehicle or insurance company- throughout the entire state of Florida, but primarily in greater central florida area for english speaking and latino community offering a 100% bilingual services ENGLISH/SPANISH and 100% remote, where I wont make clients come to an office ever, and will private online meetings, signing portals, and all to have it efficient for clients benefit.

3. Do you have an existing domain name / website address? yes, kestalaw.example through google workspace. i need help in getting in brought to you so you can handle it please.

4. In addition to a Home Page, which other pages / sections would you like your website to have:
About Us
Contact Us
Products / Services
Office / Mailing Address
Testimonials / Reviews
FAQs
Terms and Conditions
Any other page / section you would like- DO EVERYTHING IN BOTH LANGUAGES- ENGLISH AND SPANISH
I want the page to have a way for people to calendar appts with me. and also
to make transactions - accepting all methods of payment

For each of the pages / sections you’d like to have, please provide the text (and images, if available) you would like to include.

5. Which of the below are features and functionalities your website will need:
Image Gallery
Videos
Contact Form
Mailing List
Maps
FAQs
Accepting payments / donations
6. Please provide the URLs for the social media profiles you'd like to link to the website. I have none, I am just starting, I actually want to have the online presence ready before my official launch.

Target Market(s)

Injured individuals by the negligent act of another in Florida

Industry/Entity Type

LAWYER/ AUTO ACCIDENT/NEGLIGENCE/ PREMISES LIABILITY/ CIVIL LAW

Coding

Number of Pages Required

1 page

Requirements
Must have
• bilingual ENGLISH and SPANISH; a button for people to calendar appointments with me; accept payments, and to be able to integrate with major software like docusign, adobe, etc since I need to integrate under the fully remote platform
Nice to have
• look at my logo from logoforge.example it has the Vantipelle Law and KestaLaw.example together.. I have the kestalaw.example domain from google. need you guys to help integrate that too , meaning to be able to use that domain for my website.

```html
<!DOCTYPE html>
<html lang="en">
<head>
<meta charset="utf-8">
<title>Vantipelle Law — Legal Solutions for a Changing World</title>
<link href="https://fonts.googleapis.com/css2?family=Gilda+Display&family=Libre+Baskerville:ital@1&family=Plus+Jakarta+Sans:wght@400;500;600;700&display=swap" rel="stylesheet">
<style>
:root{
  --ink:#283d3a;
  --ink-card:#3c524f;
  --gold:#b8924a;
  --gold-soft:#c9a35a;
  --paper:#ffffff;
  --mist:#f0f0f0;
  --text:#3a3a3a;
  --muted:#6b6b6b;
  --line:#cfcfcf;
}
*{margin:0;padding:0;box-sizing:border-box}
html,body{width:1200px;height:3819px;overflow:hidden}
body{position:relative;font-family:"Plus Jakarta Sans",sans-serif;color:var(--text);background:var(--paper)}
a{text-decoration:none}
.abs{position:absolute}
.serif{font-family:"Gilda Display",serif;font-weight:400}
.btn{position:absolute;display:flex;align-items:center;justify-content:center;font-size:10px;font-weight:700;color:#fff;background:var(--gold)}
.btn.dark{background:var(--ink)}
.btn.ghost{background:transparent;border:1px solid #fff}
.eyebrow{position:absolute;font-size:11px;color:var(--gold);font-weight:500}
.center{text-align:center;left:0;width:1200px}

/* header + hero */
.hero{position:absolute;top:0;left:0;width:1200px;height:562px;background:linear-gradient(100deg,#d8c7ab 0%,#b8a283 28%,#6d6556 55%,#3a3c38 78%,#2a2c2a 100%)}
.hero::after{content:"";position:absolute;inset:0;background:linear-gradient(180deg,rgba(20,30,28,.35),rgba(20,30,28,.15) 40%,rgba(20,30,28,.3))}
.brand{position:absolute;left:104px;top:56px;z-index:2;color:#fff;font-size:11px;font-weight:700;letter-spacing:.5px}
.lang{position:absolute;left:250px;top:38px;z-index:2;display:flex;border:1px solid rgba(255,255,255,.6);font-size:9.5px;font-weight:700}
.lang span{padding:4px 7px;color:#fff}
.lang span.on{background:var(--gold)}
.nav{position:absolute;top:43px;z-index:2;font-size:11px;color:#fff;font-weight:500}
.nav.active{color:var(--gold-soft)}
.nav-phone{position:absolute;left:820px;top:42px;z-index:2;font-size:11px;color:#fff;font-weight:600;display:flex;align-items:center;gap:6px}
.hero-frame{position:absolute;left:200px;top:206px;width:800px;height:181px;border:1px solid rgba(255,255,255,.7);z-index:2}
.hero-title{position:absolute;left:200px;top:236px;width:800px;text-align:center;color:#fff;font-size:46px;line-height:50px;z-index:3}
.side-frame{position:absolute;left:1140px;top:466px;width:62px;height:191px;border:1px solid #c8c8c8;background:#fff;z-index:3}

/* about */
.about-blob{position:absolute;left:151px;top:766px;width:208px;height:208px;border-radius:50%;background:#e6e7e6}
.about-ring{position:absolute;left:196px;top:638px;width:296px;height:296px;border-radius:50%;border:1px solid var(--gold)}
.about-photo{position:absolute;left:250px;top:669px;width:278px;height:397px;border-radius:139px 139px 0 0;background:linear-gradient(160deg,#6f7f55 0%,#4f5c3a 35%,#8a6a3e 65%,#3e3128 100%)}
.about-h{position:absolute;left:612px;top:712px;font-size:33px;line-height:38px;color:var(--ink)}
.para{position:absolute;left:612px;width:480px;font-size:9.5px;line-height:19px;color:#4a4a4a}

/* stats */
.band-dark{position:absolute;left:0;top:1220px;width:1200px;height:729px;background:var(--ink)}
.stats{position:absolute;left:368px;top:1142px;width:832px;height:156px;background:linear-gradient(90deg,#b8924a 0%,#a88f5f 45%,#7d8378 80%,#6a7670 100%)}
.stat{position:absolute;top:40px;color:#fff}
.stat b{display:block;font-family:"Gilda Display",serif;font-weight:400;font-size:35px;line-height:40px}
.stat span{display:block;margin-top:12px;font-size:9.5px;line-height:17px;width:120px}
.stat-div{position:absolute;top:33px;width:1px;height:90px;background:rgba(255,255,255,.45)}

/* services */
.card{position:absolute;width:250px;height:155px;background:var(--ink-card);overflow:hidden}
.card svg{position:absolute;left:100px;top:28px}
.card p{position:absolute;left:0;width:100%;top:97px;text-align:center;color:#fff;font-size:13px;font-weight:500}
.card i{position:absolute;left:119px;top:122px;width:12px;height:2px;background:var(--gold)}
.card em{position:absolute;right:-14px;bottom:-14px;width:28px;height:28px;border-radius:50%;background:var(--gold)}

/* testimonials */
.testi{position:absolute;left:0;top:1949px;width:1200px;height:543px;background:var(--mist)}
.quote{position:absolute;left:290px;width:620px;top:2172px;text-align:center;font-family:"Libre Baskerville",serif;font-style:italic;font-size:14px;line-height:23px;color:#3a3a3a}
.avatar{position:absolute;top:2242px;width:68px;height:68px;border-radius:50%;border:3px solid #fff;box-shadow:0 1px 4px rgba(0,0,0,.12)}

/* faq */
.faq-row{position:absolute;left:294px;width:612px;border-top:1px solid var(--line)}
.faq-q{position:absolute;left:24px;font-size:12px;font-weight:500;color:#2b2b2b}
.faq-ico{position:absolute;left:876px;width:11px;height:11px;border-radius:50%;background:#2b2b2b;color:#fff;font-size:10px;line-height:11px;text-align:center;font-weight:700}

/* evaluation */
.eval{position:absolute;left:0;top:3043px;width:662px;height:451px;background:linear-gradient(120deg,#b58f4a 0%,#9a8a66 45%,#6f7569 100%)}
.eval-photo{position:absolute;left:662px;top:3043px;width:538px;height:451px;background:linear-gradient(135deg,#e3e1db 0%,#a9a79f 30%,#3b3a37 55%,#5a3a2a 80%,#2b2624 100%)}
.field{position:absolute;background:rgba(255,255,255,.22);border:1px solid rgba(255,255,255,.25);color:#fff;font-size:9.5px;padding:11px 12px}

/* footer */
.footer{position:absolute;left:0;top:3494px;width:1200px;height:326px;background:var(--ink)}
.f-title{position:absolute;top:3568px;color:#fff;font-size:12.5px;font-weight:500}
.f-link{position:absolute;color:#d8dcdb;font-size:10px}
.social{position:absolute;top:3673px;width:30px;height:30px;border-radius:50%;border:1px solid var(--gold)}
</style>
</head>
<body>

<!-- header & hero -->
<section class="hero" role="img" aria-label="Photo of a lawyer signing papers beside a wooden gavel on a desk"></section>
<div class="brand">VANTIPELLE LAW</div>
<div class="lang" aria-label="Language"><span class="on">EN</span><span>ES</span></div>
<a class="nav active" style="left:343px">Home</a>
<a class="nav" style="left:408px">About us</a>
<a class="nav" style="left:488px">Services</a>
<a class="nav" style="left:566px">Testimonials</a>
<a class="nav" style="left:667px">FAQs</a>
<a class="nav" style="left:728px">Contact us</a>
<div class="nav-phone"><svg width="12" height="12" viewBox="0 0 24 24" fill="none" stroke="#fff" stroke-width="2"><path d="M5 3h4l2 5-3 2a12 12 0 0 0 6 6l2-3 5 2v4a2 2 0 0 1-2 2A18 18 0 0 1 3 5a2 2 0 0 1 2-2z"/></svg>123-456-7890</div>
<a class="btn" style="left:949px;top:34px;width:144px;height:31px;z-index:2">Free Case Evaluation</a>
<div class="hero-frame"></div>
<h1 class="hero-title serif">Legal Solutions for a<br>Changing World.</h1>
<a class="btn" style="left:448px;top:369px;width:144px;height:31px;z-index:3">Free Case Evaluation</a>
<a class="btn dark" style="left:608px;top:369px;width:144px;height:31px;z-index:3">Book an Appointment</a>
<div class="side-frame"></div>

<!-- about -->
<div class="about-blob"></div>
<div class="about-ring"></div>
<svg class="abs" style="left:230px;top:671px" width="22" height="22" viewBox="0 0 22 22"><path d="M11 0L13 9 22 11 13 13 11 22 9 13 0 11 9 9z" fill="var(--gold)"/></svg>
<svg class="abs" style="left:252px;top:693px" width="10" height="10" viewBox="0 0 22 22"><path d="M11 0L13 9 22 11 13 13 11 22 9 13 0 11 9 9z" fill="var(--ink)"/></svg>
<div class="about-photo" role="img" aria-label="Photo of a bronze justice statue holding scales beside a gavel"></div>
<div class="eyebrow" style="left:612px;top:683px">About Us</div>
<h2 class="about-h serif">We Are Here to Manage Your<br>Law with Experience</h2>
<p class="para" style="top:810px">Vantipelle Law is a solo injury practice serving Florida and D.C., with New York coming soon. If you were hurt in a crash, on a boat or on someone else's property, we help you claim what you are owed from the at-fault party or the insurance company.</p>
<p class="para" style="top:886px">We are 100% remote and 100% bilingual, English and Spanish. You never need to visit an office: meet privately online, sign documents through secure e-signing portals, book appointments and pay online.</p>
<a class="btn dark" style="left:612px;top:994px;width:104px;height:29px">Explore More</a>

<!-- stats -->
<div class="band-dark"></div>
<div class="stats">
  <div class="stat" style="left:121px"><b>1.3K+</b><span>Injury cases reviewed for our clients</span></div>
  <div class="stat-div" style="left:296px"></div>
  <div class="stat" style="left:373px"><b>55+</b><span>Florida cities served fully remote</span></div>
  <div class="stat-div" style="left:549px"></div>
  <div class="stat" style="left:626px"><b>12+</b><span>Years of legal practice experience</span></div>
</div>

<!-- services -->
<div class="eyebrow center" style="top:1375px">Our Services</div>
<h2 class="abs serif center" style="top:1403px;font-size:35px;color:#fff">Legal Practice Area</h2>

<div class="card" style="left:200px;top:1474px">
  <svg width="50" height="46" viewBox="0 0 50 46" fill="none" stroke="#fff" stroke-width="1.6"><path d="M4 34V26l5-9h22l6 9h7v8z"/><circle cx="13" cy="35" r="4"/><circle cx="36" cy="35" r="4"/><path d="M12 19l-2 6h10v-6M24 19v6h9l-4-6z"/><path d="M44 8v24M40 4l2 4M47 4l-2 4" stroke="var(--gold)"/></svg>
  <p>Auto Accidents</p><i></i><em></em></div>
<div class="card" style="left:475px;top:1474px">
  <svg width="50" height="46" viewBox="0 0 50 46" fill="none" stroke="#fff" stroke-width="1.6"><circle cx="22" cy="22" r="9"/><path d="M22 6v5M22 33v5M6 22h5M33 22h5M11 11l3 3M30 30l3 3M11 33l3-3M30 14l3-3"/><path d="M36 28l7 12H29z" fill="var(--gold)" stroke="var(--gold)"/></svg>
  <p>Negligence</p><i></i><em></em></div>
<div class="card" style="left:750px;top:1474px">
  <svg width="50" height="46" viewBox="0 0 50 46" fill="none" stroke="#fff" stroke-width="1.6"><path d="M8 30l28-16 6 8-26 14z" fill="var(--gold)" stroke="var(--gold)"/><path d="M14 22V10l12 10"/><path d="M3 40q5-4 10 0t11 0 11 0 11 0"/></svg>
  <p>Boat Accident</p><i></i><em></em></div>
<div class="card" style="left:200px;top:1655px">
  <svg width="50" height="46" viewBox="0 0 50 46" fill="none" stroke="#fff" stroke-width="1.6"><circle cx="8" cy="34" r="5"/><circle cx="22" cy="34" r="5"/><path d="M8 34l6-10h8l4 10M14 24l-3-5h6"/><rect x="30" y="14" width="18" height="20" fill="var(--gold)" stroke="var(--gold)"/><path d="M36 4l-4 8h6l-3 8"/></svg>
  <p>Motorcycle Accident</p><i></i><em></em></div>
<div class="card" style="left:475px;top:1655px">
  <svg width="50" height="46" viewBox="0 0 50 46" fill="none" stroke="#fff" stroke-width="1.6"><path d="M12 4h18l6 6v30H12z"/><path d="M17 14h10M17 20h14M17 26h8"/><path d="M34 24l8 3v6c0 4-4 7-8 8-4-1-8-4-8-8v-6z" fill="var(--gold)" stroke="var(--gold)"/></svg>
  <p>Insurance Claims</p><i></i><em></em></div>
<div class="card" style="left:750px;top:1655px">
  <svg width="50" height="46" viewBox="0 0 50 46" fill="none" stroke="#fff" stroke-width="1.6"><path d="M34 4l12 20H22z" fill="var(--gold)" stroke="var(--gold)"/><path d="M6 42h28M12 36l6-10M18 26l8 4"/><circle cx="12" cy="16" r="3"/></svg>
  <p>Premises liability</p><i></i><em></em></div>

<a class="btn" style="left:549px;top:1843px;width:102px;height:30px">Explore More</a>

<!-- testimonials -->
<section class="testi"></section>
<div class="eyebrow center" style="top:2025px">Testimonials</div>
<h2 class="abs serif center" style="top:2053px;font-size:35px;color:var(--ink)">What Our Clients Say</h2>
<div class="abs serif center" style="top:2108px;font-size:70px;line-height:70px;color:var(--gold)">&ldquo;</div>
<p class="quote">&ldquo;I never had to leave home. Every meeting was online and in Spanish, and my claim against the insurer was settled fairly.&rdquo;</p>
<svg class="abs" style="left:198px;top:2185px" width="14" height="22" viewBox="0 0 14 22" fill="none" stroke="#2b2b2b" stroke-width="1.6"><path d="M12 1L2 11l10 10"/></svg>
<svg class="abs" style="left:988px;top:2185px" width="14" height="22" viewBox="0 0 14 22" fill="none" stroke="#2b2b2b" stroke-width="1.6"><path d="M2 1l10 10L2 21"/></svg>
<div class="avatar" style="left:475px;background:#d6d2cc" role="img" aria-label="Client portrait"></div>
<div class="avatar" style="left:565px;background:#d9b98f" role="img" aria-label="Client portrait"></div>
<div class="avatar" style="left:662px;background:#cdb08a" role="img" aria-label="Client portrait"></div>
<div class="abs" style="left:614px;top:2294px;width:16px;height:16px;border-radius:50%;background:var(--gold);border:2px solid #fff"></div>
<div class="abs center" style="top:2329px;font-size:11.5px;font-weight:700;color:#2b2b2b">Maria Delgado</div>
<div class="abs center" style="top:2346px;font-size:9.5px;color:var(--muted)">Auto accident client, Orlando</div>
<a class="btn dark" style="left:528px;top:2386px;width:144px;height:31px">View All Testimonials</a>

<!-- faq -->
<h2 class="abs serif center" style="top:2564px;font-size:36px;color:var(--ink)">Frequently Asked Questions</h2>
<div class="faq-row" style="top:2638px;height:39px"><span class="faq-q" style="top:14px">Do I ever need to visit an office?</span></div>
<div class="faq-ico" style="top:2651px">+</div>
<div class="faq-row" style="top:2677px;height:111px;background:#f3f3f3;border-top:0">
  <span class="faq-q" style="top:14px">Can I get help in Spanish?</span>
  <p class="abs" style="left:24px;top:45px;width:560px;font-size:9px;line-height:15px;color:#555">Yes. Every service is offered fully in English and Spanish, from your first consultation to the final settlement. Calls, online meetings, documents and e-signing portals are all available in the language you prefer, so nothing gets lost in translation.</p>
</div>
<div class="faq-ico" style="top:2690px;background:var(--gold)">&minus;</div>
<div class="faq-row" style="top:2788px;height:39px"><span class="faq-q" style="top:15px">How do I book an appointment and pay online?</span></div>
<div class="faq-ico" style="top:2804px">+</div>
<div class="faq-row" style="top:2827px;height:38px"><span class="faq-q" style="top:15px">What should I do right after a car accident?</span></div>
<div class="faq-ico" style="top:2843px">+</div>
<div class="faq-row" style="top:2865px;height:39px;border-bottom:1px solid var(--line)"><span class="faq-q" style="top:15px">How much does a free case evaluation cost?</span></div>
<div class="faq-ico" style="top:2881px">+</div>
<a class="btn dark" style="left:561px;top:2935px;width:77px;height:31px">View All</a>

<!-- evaluation form -->
<section class="eval"></section>
<div class="eval-photo" role="img" aria-label="Photo of a lawyer in a suit at a desk with scales of justice and a gavel"></div>
<h2 class="abs serif" style="left:107px;top:3113px;font-size:30px;color:#fff">Free Case Evaluation</h2>
<p class="abs" style="left:107px;top:3161px;font-size:11px;color:#fff">Fill out the form below and we will contact you during our working hours.</p>
<div class="field" style="left:107px;top:3203px;width:233px;height:30px;padding-top:9px">Name</div>
<div class="field" style="left:353px;top:3203px;width:234px;height:30px;padding-top:9px">Phone</div>
<div class="field" style="left:107px;top:3246px;width:233px;height:30px;padding-top:9px">Email...</div>
<div class="field" style="left:353px;top:3246px;width:234px;height:30px;padding-top:9px">Select your Services</div>
<div class="field" style="left:107px;top:3289px;width:480px;height:88px">How can we help you?</div>
<a class="btn" style="left:107px;top:3390px;width:71px;height:30px;background:#fff;color:#2b2b2b">Submit</a>
<a class="btn ghost" style="left:190px;top:3390px;width:96px;height:30px">Make a Payment</a>

<!-- footer -->
<footer class="footer"></footer>
<div class="abs" style="left:199px;top:3630px;font-size:15px;font-weight:700;color:#fff;letter-spacing:.5px">VANTIPELLE LAW</div>
<div class="social" style="left:225px"></div>
<div class="social" style="left:262px"></div>
<div class="social" style="left:299px"></div>

<div class="f-title" style="left:451px">Contct us</div>
<div class="f-link" style="left:451px;top:3605px;font-size:11px;display:flex;gap:9px;align-items:center"><svg width="11" height="11" viewBox="0 0 24 24" fill="none" stroke="#fff" stroke-width="2"><path d="M5 3h4l2 5-3 2a12 12 0 0 0 6 6l2-3 5 2v4a2 2 0 0 1-2 2A18 18 0 0 1 3 5a2 2 0 0 1 2-2z"/></svg>123-456-7890</div>
<div class="f-link" style="left:451px;top:3638px;font-size:11px;display:flex;gap:9px;align-items:center"><svg width="11" height="11" viewBox="0 0 24 24" fill="none" stroke="#fff" stroke-width="2"><rect x="2" y="5" width="20" height="14"/><path d="M2 5l10 8 10-8"/></svg>info@vantipellelaw.example</div>
<div class="f-link" style="left:451px;top:3669px;font-size:11px;display:flex;gap:9px;line-height:15px"><svg width="11" height="13" viewBox="0 0 24 28" fill="none" stroke="#fff" stroke-width="2" style="margin-top:2px"><path d="M12 27s9-9 9-15a9 9 0 0 0-18 0c0 6 9 15 9 15z"/><circle cx="12" cy="12" r="3"/></svg><span>226 Orange Blossom Ave, Suite 4,<br>Orlando, FL 32801</span></div>
<div class="f-link" style="left:451px;top:3716px;color:var(--gold);font-weight:600">Get Directions &nearr;</div>

<div class="f-title" style="left:703px">Quick links</div>
<div class="f-link" style="left:703px;top:3603px">Home</div>
<div class="f-link" style="left:703px;top:3626px">About Us</div>
<div class="f-link" style="left:703px;top:3648px">Book Appointment</div>
<div class="f-link" style="left:703px;top:3670px">Make a Payment</div>
<div class="f-link" style="left:703px;top:3693px">FAQs</div>
<div class="f-link" style="left:703px;top:3715px">Contact Us</div>

<div class="f-title" style="left:870px">Services</div>
<div class="f-link" style="left:870px;top:3603px">Auto Accidents</div>
<div class="f-link" style="left:870px;top:3626px">Negligence</div>
<div class="f-link" style="left:870px;top:3648px">Boat Accident</div>
<div class="f-link" style="left:870px;top:3670px">Motorcycle Accident</div>
<div class="f-link" style="left:870px;top:3693px">Insurance Claims</div>
<div class="f-link" style="left:870px;top:3715px">Premises Liability</div>

<div class="abs" style="left:200px;top:3762px;width:800px;height:1px;background:rgba(255,255,255,.2)"></div>
<div class="f-link" style="left:200px;top:3785px">&copy; 2025 <span style="color:var(--gold)">Vantipelle Law.</span> All rights reserved.</div>
<div class="f-link" style="left:451px;top:3785px">Terms and Condition</div>
<div class="abs" style="left:1074px;top:3745px;width:32px;height:32px;border-radius:50%;border:1px solid #9aa6a4;display:flex;align-items:center;justify-content:center"><svg width="10" height="12" viewBox="0 0 10 12" fill="none" stroke="#fff" stroke-width="1.4"><path d="M5 11V1M1 5l4-4 4 4"/></svg></div>

</body>
</html>
```